Property Management business needs Business cards designed

We provide a premium property management service based in Sydney's Norther Beaches. We want people to feel confident in choosing us to manage their investment properties. We offer a much more personalized service than other estate agents.
We want a modern clean design. Something that shows confidence without being complicated.
Logo attached.

Target Market(s)

35-70yo Male and Female with strong property portfolios within Sydney's Norther Beaches

Industry/Entity Type

Property Management

Contact Information for Business Card

Address: Suite 7, 12-14 Kelvin Parade, Harlow NSW 2188
Two separate named cards.
Tom Ardley - 0491 570 118 tom@harbourvaleestates.com.au
Clara Dunmore - 0491 570 263 clara@harbourvaleestates.com.au

Requirements
Must have
• Business logo, name, number, address, email.

```html
<!DOCTYPE html>
<html lang="en">
<head>
<meta charset="UTF-8">
<title>Harbourvale Estates – Business Cards</title>
<link rel="stylesheet" href="https://fonts.googleapis.com/css2?family=Open+Sans:wght@400;600;700&display=swap">
<style>
  :root {
    --page-bg: #e9e6e1;
    --card-bg: #ffffff;
    --ink: #1f2326;
    --ink-soft: #2b2f33;
    --teal: #2b9ba8;
    --divider: #6b4632;
  }
  * { margin: 0; padding: 0; box-sizing: border-box; }
  html, body {
    width: 1200px;
    height: 780px;
    overflow: hidden;
    background: var(--page-bg);
    font-family: "Open Sans", Arial, sans-serif;
    color: var(--ink);
  }
  .card-set {
    position: absolute;
    left: 25px;
    top: 230px;
    display: flex;
    gap: 30px;
  }
  .card {
    position: relative;
    width: 560px;
    height: 320px;
    background: var(--card-bg);
    box-shadow: 0 8px 24px rgba(0,0,0,0.12);
  }
  .brand {
    position: absolute;
    right: 40px;
    top: 58px;
    display: flex;
    align-items: center;
    gap: 11px;
  }
  .brand-dot {
    width: 21px;
    height: 21px;
    border-radius: 50%;
    background: var(--teal);
  }
  .brand-name {
    font-size: 31px;
    font-weight: 700;
    letter-spacing: 0.3px;
    line-height: 1;
    text-transform: uppercase;
    color: var(--ink);
    white-space: nowrap;
  }
  .name-row {
    position: absolute;
    left: 38px;
    right: 24px;
    top: 166px;
    display: flex;
    align-items: center;
    gap: 12px;
  }
  .holder-name {
    font-size: 22px;
    font-weight: 700;
    line-height: 1.2;
    color: var(--teal);
    white-space: nowrap;
  }
  .divider {
    flex: 1;
    height: 1px;
    background: var(--divider);
  }
  .contact {
    position: absolute;
    left: 38px;
    top: 218px;
    list-style: none;
  }
  .contact-item {
    display: flex;
    align-items: center;
    gap: 10px;
    height: 25px;
    font-size: 14px;
    color: var(--ink-soft);
    white-space: nowrap;
  }
  .contact-icon {
    width: 19px;
    height: 19px;
    flex: none;
  }
  .address {
    position: absolute;
    right: 40px;
    top: 218px;
    text-align: right;
    font-style: normal;
    font-size: 14px;
    line-height: 25px;
    color: var(--ink-soft);
    white-space: nowrap;
  }
</style>
</head>
<body>
  <div class="card-set">
    <section class="card">
      <div class="brand">
        <span class="brand-dot"></span>
        <span class="brand-name">Harbourvale Estates</span>
      </div>
      <div class="name-row">
        <h1 class="holder-name">Tom Ardley</h1>
        <span class="divider"></span>
      </div>
      <ul class="contact">
        <li class="contact-item">
          <svg class="contact-icon" viewBox="0 0 30 30" aria-hidden="true">
            <rect width="30" height="30" fill="var(--teal)"/>
            <path d="M9 7 L13 7 L14 11 L12 13 Q14 17 17 18 L19 16 L23 17 L23 21 Q21 23 18 22 Q10 19 8 11 Q7 8 9 7 Z" fill="#fff"/>
          </svg>
          <span>0491 570 118</span>
        </li>
        <li class="contact-item">
          <svg class="contact-icon" viewBox="0 0 30 30" aria-hidden="true">
            <rect width="30" height="30" fill="var(--teal)"/>
            <rect x="6" y="9" width="18" height="12" fill="none" stroke="#fff" stroke-width="1.8"/>
            <path d="M6 9 L15 16 L24 9 M6 21 L12.5 14.5 M24 21 L17.5 14.5" fill="none" stroke="#fff" stroke-width="1.6"/>
          </svg>
          <span>tom@harbourvaleestates.com.au</span>
        </li>
      </ul>
      <address class="address">
        Suite 7, 12-14 Kelvin Parade<br>
        Harlow NSW 2188
      </address>
    </section>

    <section class="card">
      <div class="brand">
        <span class="brand-dot"></span>
        <span class="brand-name">Harbourvale Estates</span>
      </div>
      <div class="name-row">
        <h1 class="holder-name">Clara Dunmore</h1>
        <span class="divider"></span>
      </div>
      <ul class="contact">
        <li class="contact-item">
          <svg class="contact-icon" viewBox="0 0 30 30" aria-hidden="true">
            <rect width="30" height="30" fill="var(--teal)"/>
            <path d="M9 7 L13 7 L14 11 L12 13 Q14 17 17 18 L19 16 L23 17 L23 21 Q21 23 18 22 Q10 19 8 11 Q7 8 9 7 Z" fill="#fff"/>
          </svg>
          <span>0491 570 263</span>
        </li>
        <li class="contact-item">
          <svg class="contact-icon" viewBox="0 0 30 30" aria-hidden="true">
            <rect width="30" height="30" fill="var(--teal)"/>
            <rect x="6" y="9" width="18" height="12" fill="none" stroke="#fff" stroke-width="1.8"/>
            <path d="M6 9 L15 16 L24 9 M6 21 L12.5 14.5 M24 21 L17.5 14.5" fill="none" stroke="#fff" stroke-width="1.6"/>
          </svg>
          <span>clara@harbourvaleestates.com.au</span>
        </li>
      </ul>
      <address class="address">
        Suite 7, 12-14 Kelvin Parade<br>
        Harlow NSW 2188
      </address>
    </section>
  </div>
</body>
</html>
```